Harbor Relay Group Letterhead Design

The project name sums it up. Just need a professional letterhead design / template we can use in our marketing folders.

Here's the address / contact info for the letterhead: Harbor Relay Group 4815 Maple Crest Ave Suite 210 League City, Texas 77419 346-507-3846 www.harborrelaygroup.us support@harborrelaygroup.us

```html
<!DOCTYPE html>
<html lang="en">
<head>
<meta charset="utf-8">
<title>Harbor Relay Group Letterhead</title>
<link href="https://fonts.googleapis.com/css2?family=Arimo:wght@400;700&display=swap" rel="stylesheet">
<style>
  :root {
    --backdrop: #d9cbb0;
    --paper: #ffffff;
    --ink: #1a1a1a;
    --brand-blue: #1f5fb8;
    --band-black: #0d0d0d;
    --muted: #555555;
  }
  * { box-sizing: border-box; margin: 0; padding: 0; }
  html, body { width: 1200px; height: 898px; overflow: hidden; }
  body {
    background: var(--backdrop);
    font-family: "Arimo", Arial, sans-serif;
    color: var(--ink);
    position: relative;
  }
  .letterhead {
    position: absolute;
    left: 303px; top: 29px;
    width: 594px; height: 840px;
    background: var(--paper);
    box-shadow: 0 6px 24px rgba(0,0,0,0.18);
    overflow: hidden;
  }
  .masthead {
    position: absolute;
    top: 62px; left: 0; right: 0;
    display: flex; justify-content: center; align-items: center; gap: 10px;
  }
  .masthead-mark {
    width: 26px; height: 26px; background: var(--ink);
  }
  .masthead-name {
    font-weight: 700; font-size: 24px; letter-spacing: 0.5px; color: var(--ink);
  }
  .letter {
    position: absolute;
    left: 62px; top: 268px; width: 440px;
    font-size: 9.6px; line-height: 1.32;
  }
  .recipient { margin-bottom: 12px; }
  .recipient strong { font-weight: 700; }
  .letter p { margin-bottom: 12px; }
  .closing { margin-top: 20px; }
  .signature {
    display: block;
    width: 110px; height: 34px; margin-top: 14px;
    background: linear-gradient(90deg, #e8e8e8, #d6d6d6);
    border-radius: 4px;
  }
  .footer-art { position: absolute; left: 0; bottom: 0; }
  .footer-heading {
    position: absolute; left: 46px; bottom: 96px;
    font-weight: 700; font-size: 14px; letter-spacing: 1px;
    color: var(--brand-blue); text-transform: uppercase;
  }
  .footer-address {
    position: absolute; left: 46px; bottom: 62px;
    font-size: 10.5px; color: #fff;
  }
  .footer-contacts {
    position: absolute; left: 46px; bottom: 42px;
    display: flex; align-items: center; gap: 10px;
    font-size: 9px; color: #fff;
  }
  .footer-contacts svg { width: 10px; height: 10px; vertical-align: -1px; margin-right: 5px; }
  .divider { width: 1px; height: 11px; background: #fff; }
  .footer-web {
    position: absolute; right: 22px; bottom: 108px;
    font-size: 9px; color: #fff;
  }
  .corner-mark {
    position: absolute; right: 22px; bottom: 138px;
    width: 58px; height: 58px; border-radius: 50%;
    background: var(--ink);
  }
</style>
</head>
<body>
  <main class="letterhead">
    <header class="masthead">
      <span class="masthead-mark"></span>
      <span class="masthead-name">Harbor Relay Group</span>
    </header>

    <section class="letter">
      <div class="recipient">
        <strong>Someone Some body</strong><br>
        1001 Long Street<br>
        New York City, USA
      </div>
      <p>Dear Someone Somebody,</p>
      <p>Lorem ipsum dolor sit amet, consectetur adipiscing elit. Nunc ac magna tellus, vitae hendrerit mauris. Donec consectetur rhoncus nunc, vitae imperdiet leo viverra ut. Pellentesque fermentum mi ac erat ultricies faucibus. Nam gravida nibh non lacus fermentum porta. Nulla non placerat turpis. Maecenas quis metus sem. Nullam nisi lacus, egestas sit amet porttitor nec, consectetur eget neque. Vivamus ultricies ultrices turpis, vel porttitor odio sagittis a. Pellentesque accumsan, lacus at suscipit rutrum, erat tortor imperdiet purus, semper congue augue turpis eget est. Curabitur blandit, orci ut accumsan fermentum, lorem metus auctor nisl, eget sodales elit libero id mi. Nullam sed lorem augue, ut tristique dui.</p>
      <p>Pellentesque vehicula pulvinar libero et ultricies. In hac habitasse platea dictumst. Phasellus eget quam lectus, pellentesque condimentum nulla. Morbi consequat euismod purus ut auctor. Cras convallis eleifend vehicula. Sed facilisis egestas accumsan. Duis in blandit velit. Curabitur diam eros, volutpat et iaculis ut, suscipit at est.</p>
      <p>Aenean id diam enim. Donec vitae arcu quam. Nunc mollis feugiat pretium. Praesent vel ligula felis. Ut sed velit nibh. Suspendisse faucibus convallis scelerisque. Sed sodales, nisi vitae placerat eleifend, lorem nulla iaculis leo, in lacinia metus sem quis purus. Ut non felis felis, pharetra fermentum purus. Suspendisse potenti. Nunc non faucibus ligula. Phasellus ipsum velit, laoreet ut scelerisque vel, commodo at felis. Donec malesuada malesuada aliquam. Aliquam justo elit, dapibus vitae hendrerit hendrerit, commodo sed ipsum. Donec ultricies mi non felis sollicitudin et elementum augue adipiscing. Integer quam purus, venenatis in ornare ac, sagittis quis purus.</p>
      <p class="closing">Youre Sincerely,</p>
      <span class="signature" role="img" aria-label="Handwritten signature"></span>
    </section>

    <span class="corner-mark"></span>

    <svg class="footer-art" width="594" height="140" viewBox="0 0 594 140" aria-hidden="true">
      <polygon points="0,60 420,60 400,140 0,140" fill="var(--band-black)"/>
      <polygon points="0,60 420,60 418,66 0,66" fill="var(--band-black)"/>
      <polygon points="438,10 594,10 594,36 430,36" fill="var(--brand-blue)"/>
    </svg>

    <div class="footer-heading">Harbor Relay Group</div>
    <div class="footer-address">4815 Maple Crest Ave Suite 210 League City, Texas 77419</div>
    <div class="footer-contacts">
      <span><svg viewBox="0 0 24 24"><path fill="#fff" d="M6.6 10.8a15 15 0 0 0 6.6 6.6l2.2-2.2c.3-.3.7-.4 1-.2 1.1.4 2.3.6 3.6.6.6 0 1 .4 1 1V20c0 .6-.4 1-1 1A17 17 0 0 1 3 4c0-.6.4-1 1-1h3.5c.6 0 1 .4 1 1 0 1.3.2 2.5.6 3.6.1.3 0 .7-.2 1z"/></svg>346-507-3846</span>
      <span class="divider"></span>
      <span><svg viewBox="0 0 24 24"><path fill="#fff" d="M2 5h20v14H2zm2 2v.5l8 5 8-5V7zm0 2.8V17h16V9.8l-8 5z"/></svg>support@harborrelaygroup.us</span>
    </div>
    <div class="footer-web">www.harborrelaygroup.us</div>
  </main>
</body>
</html>
```